Morvex Business Card (intended for Business Card sized magnet)

Hi guys,

I would like to get a design for my business card for the restaurant. The design must be single sided as I intend to produce business card sized magnets.

The File attached must me on and I'm open for new ides

Can you please ensure that the design meets Cardowell's magnetic business card size specifications:

http://www.cardowell.example.au/custom-magnets.aspx?txi=15695&xnid=TopNav_Magnetic+Business+Cards+(linked+item)_Magnets_Marketing+Products&xnav=TopNav

Full Bleed Size (starting document size):
90 x 52 mm
1062 x 615 pixels
* Finished artwork should use the full bleed dimensions for best results.

Document Trim Size (final size after being cut):
87 x 49 mm
1028 x 579 pixels
* Please be sure to keep all text within the safe margin.

Resolution:
300 DPI

The winning design/source files need to meet these specifications.

Thanks
Updates

Hi guys, can I see more options please Thanks

```html
<!DOCTYPE html>
<html lang="en">
<head>
<meta charset="utf-8">
<title>Morvex Business Card</title>
<link rel="stylesheet" href="https://fonts.googleapis.com/css2?family=Alegreya:wght@400;500&display=swap">
<style>
  :root {
    --paper: #ffffff;
    --ink: #1c1c1c;
    --accent-red: #c8202f;
    --accent-teal: #1aa3bd;
    --accent-yellow: #f2b705;
    --band: #2a2a2a;
  }
  html, body {
    margin: 0;
    padding: 0;
    width: 1200px;
    height: 686px;
    overflow: hidden;
    background: var(--paper);
  }
  .card {
    position: relative;
    width: 1200px;
    height: 686px;
    background: var(--paper);
    font-family: "Alegreya", Georgia, serif;
    color: var(--ink);
  }
  .brand-name {
    position: absolute;
    left: 55px;
    top: 62px;
    margin: 0;
    font-size: 122px;
    font-weight: 400;
    line-height: 1;
    letter-spacing: 1px;
    color: #000;
  }
  .brand-band {
    position: absolute;
    left: 46px;
    top: 207px;
    width: 366px;
    height: 124px;
    background: var(--band);
  }
  .contact-item {
    position: absolute;
    display: flex;
    align-items: center;
    font-size: 38px;
    line-height: 1;
    white-space: nowrap;
  }
  .contact-item svg {
    flex: none;
  }
  .contact-phone { left: 40px; top: 462px; }
  .contact-web   { left: 40px; top: 534px; }
  .contact-email { left: 40px; top: 606px; }
  .contact-phone span,
  .contact-web span,
  .contact-email span { margin-left: 22px; }
  .address {
    position: absolute;
    left: 758px;
    top: 462px;
    display: flex;
    align-items: flex-start;
    font-size: 38px;
    line-height: 72px;
  }
  .address svg { margin-top: 4px; }
  .address p { margin: -18px 0 0 24px; }
</style>
</head>
<body>
<div class="card">
  <h1 class="brand-name">Morvex</h1>
  <div class="brand-band" role="img" aria-label="Geometric star pattern band with red, teal and yellow accents"></div>

  <div class="contact-item contact-phone">
    <svg width="36" height="36" viewBox="0 0 24 24" aria-hidden="true">
      <path fill="var(--accent-red)" d="M6.6 10.8c1.4 2.8 3.8 5.1 6.6 6.6l2.2-2.2c.3-.3.7-.4 1-.2 1.1.4 2.3.6 3.6.6.6 0 1 .4 1 1V20c0 .6-.4 1-1 1C10.6 21 3 13.4 3 4c0-.6.4-1 1-1h3.5c.6 0 1 .4 1 1 0 1.3.2 2.5.6 3.6.1.3 0 .7-.2 1z"/>
    </svg>
    <span>03 9418 2730</span>
  </div>

  <div class="contact-item contact-web">
    <svg width="38" height="34" viewBox="0 0 24 22" aria-hidden="true">
      <rect x="1.5" y="1.5" width="21" height="13" rx="1" fill="#bfe9f2" stroke="var(--accent-teal)" stroke-width="2"/>
      <rect x="10" y="15" width="4" height="4" fill="var(--accent-teal)"/>
      <rect x="6" y="19" width="12" height="2" fill="var(--accent-teal)"/>
    </svg>
    <span>www.morvex.com.au</span>
  </div>

  <div class="contact-item contact-email">
    <svg width="38" height="28" viewBox="0 0 24 17" aria-hidden="true">
      <rect x="0.5" y="0.5" width="23" height="16" fill="var(--accent-yellow)"/>
      <path d="M1 1l11 9 11-9M1 16l8-7M23 16l-8-7" fill="none" stroke="#fff" stroke-width="1.4"/>
    </svg>
    <span>Morvex678@mailnest.com</span>
  </div>

  <div class="address">
    <svg width="26" height="36" viewBox="0 0 16 22" aria-hidden="true">
      <path fill="var(--accent-red)" d="M8 0C3.6 0 0 3.5 0 7.9 0 13.8 8 22 8 22s8-8.2 8-14.1C16 3.5 12.4 0 8 0zm0 11a3 3 0 1 1 0-6 3 3 0 0 1 0 6z"/>
    </svg>
    <p>412 Brennan st,<br>ashvale north, 3174</p>
  </div>
</div>
</body>
</html>
```